Dream Vacation 2025

Brightfield Autos is Hosting a campaign giving away a dream vacation ( travel voucher) valued at 5000.00. Every person that buys a vehicle from us during the month of December and January receives an entry to win.

I need a cover photo for facebook. multiple facebook/instagram posts. flyers that i can print and a banner for my website. All I would like to have my company logo on all campaign pieces. I would also like a landing page designed for my website with graphics and descriptions I do not want the year posted on any of the graphics so that i can reuse these in the future.

brightfieldautos.com

```html
<!DOCTYPE html>
<html lang="en">
<head>
<meta charset="utf-8">
<title>Brightfield Autos – Travel Voucher Campaign</title>
<link rel="stylesheet" href="https://fonts.googleapis.com/css2?family=Cinzel:wght@700&family=Mulish:wght@400;500&family=Montserrat:wght@700&display=swap">
<style>
  :root {
    --paper: #ffffff;
    --ink: #1a1a1a;
    --gold-dark: #b8801e;
    --gold-mid: #e2b52c;
    --gold-light: #fbe44f;
    --band-dark: #2f3334;
    --band-mid: #4a4f50;
    --photo-top: #6fb6d6;
    --photo-bottom: #cfe3ea;
    --ornament: #3a3a3a;
    --headline: #ffffff;
  }
  * { margin: 0; padding: 0; box-sizing: border-box; }
  html, body { width: 1200px; height: 1047px; overflow: hidden; background: var(--paper); }
  .canvas { position: relative; width: 1200px; height: 1047px; background: var(--paper); overflow: hidden; }
  .artwork { position: absolute; inset: 0; }

  .brand { position: absolute; left: 40px; top: 150px; width: 320px; text-align: center; color: var(--ink); }
  .brand-name { font-family: "Montserrat", sans-serif; font-weight: 700; font-size: 24px; letter-spacing: 1.5px; line-height: 1; white-space: nowrap; }
  .brand-place { font-family: "Montserrat", sans-serif; font-weight: 700; font-size: 10px; letter-spacing: 2.5px; margin-top: 9px; }

  .headline { position: absolute; left: 95px; top: 300px; width: 430px; text-align: center;
    font-family: "Cinzel", serif; font-weight: 700; color: var(--headline);
    font-size: 62px; line-height: 78px; }

  .details { position: absolute; left: 58px; top: 712px; width: 600px;
    font-family: "Mulish", sans-serif; font-size: 22px; line-height: 39px; color: var(--ink); white-space: nowrap; }
  .details p + p { margin-top: 39px; }
</style>
</head>
<body>
<main class="canvas">
  <svg class="artwork" width="1200" height="1047" viewBox="0 0 1200 1047" xmlns="http://www.w3.org/2000/svg">
    <defs>
      <linearGradient id="gold" x1="0" y1="0" x2="1" y2="0">
        <stop offset="0" stop-color="var(--gold-dark)"/>
        <stop offset="0.55" stop-color="var(--gold-light)"/>
        <stop offset="1" stop-color="var(--gold-dark)"/>
      </linearGradient>
      <linearGradient id="gold-bottom" x1="0" y1="0" x2="1" y2="0">
        <stop offset="0" stop-color="var(--gold-dark)"/>
        <stop offset="0.6" stop-color="var(--gold-mid)"/>
        <stop offset="1" stop-color="var(--gold-light)"/>
      </linearGradient>
      <linearGradient id="band" x1="0" y1="0" x2="0" y2="1">
        <stop offset="0" stop-color="var(--band-dark)"/>
        <stop offset="1" stop-color="var(--band-mid)"/>
      </linearGradient>
      <linearGradient id="photo-tone" x1="0" y1="0" x2="0" y2="1">
        <stop offset="0" stop-color="var(--photo-top)"/>
        <stop offset="1" stop-color="var(--photo-bottom)"/>
      </linearGradient>
    </defs>

    <path class="deco-arch" d="M744 140 A40 40 0 0 1 824 140 Z M752 140 A32 32 0 0 1 816 140" fill="none" stroke="var(--ink)" stroke-width="2.5"/>
    <circle class="deco-ring" cx="1077" cy="150" r="28" fill="none" stroke="var(--ink)" stroke-width="14"/>
    <path class="deco-wave" d="M1031 214 q7 -6 14 0 t14 0 t14 0 t14 0 t14 0 t12 0" fill="none" stroke="var(--ink)" stroke-width="3"/>

    <rect class="scenic-band" x="0" y="262" width="860" height="397" fill="url(#band)" role="img" aria-label="Dim seaside backdrop with clouds over the water"/>
    <path class="scenic-panel" d="M700 480 H1200 V878 H930 Q760 878 700 700 Z" fill="url(#band)" role="img" aria-label="Dim coastal backdrop with greenery and rocks"/>

    <path class="gold-band-top" d="M0 220 H847 A293 293 0 0 1 1112 442 A262 262 0 0 0 847 262 H0 Z" fill="url(#gold)"/>
    <path class="gold-band-bottom" d="M667 711 Q720 920 930 920 H1200 V878 H930 Q770 878 700 700 Z" fill="url(#gold-bottom)"/>

    <circle class="feature-photo" cx="847" cy="513" r="256" fill="url(#photo-tone)" stroke="var(--paper)" stroke-width="5" role="img" aria-label="Photo: teal SUV parked on a sandy beach by the sea under a blue sky"/>

    <path class="deco-dots" d="M697 996 A40 40 0 0 1 777 996 Z" fill="var(--ornament)" opacity="0.8" role="img" aria-label="Dotted half-circle ornament"/>
  </svg>

  <div class="brand">
    <div class="brand-name">BRIGHTFIELD AUTOS</div>
    <div class="brand-place">- PINE RIDGE, AB -</div>
  </div>

  <h1 class="headline">WIN A<br>$ 5,000<br>TRAVEL<br>VOUCHER!</h1>

  <section class="details">
    <p>Brightfield Autos is hosting a campaign giving<br>away a Dream Vacation Travel Voucher valued<br>at $5,000!</p>
    <p>Every person who buys a vehicle from us during<br>the months of December and January receives<br>an entry to win.</p>
  </section>
</main>
</body>
</html>
```